Business card - Kestrel Bay Framing

Design a business card utilizing the given logo.
colors we like: Black, greys, Teal, blues.
Tri color card, horizontal orientation likely
Logo and name likely best on top.
Info on card:

Dennis Harcourt
#5 - 1845 Larchmont Way
Surrey, B.C. V7T 3K2

604.555.0193
dennisharcourt@telvane.ca

Slogan: "Building Dreams"

We are a construction company that specializes in new home construction on the West coast of BC Canada. Bay Framing designs of high end homes.

```html
<!DOCTYPE html>
<html lang="en">
<head>
<meta charset="utf-8">
<title>Kestrel Bay Framing – Business Card</title>
<link href="https://fonts.googleapis.com/css2?family=Questrial&display=swap" rel="stylesheet">
<style>
  :root {
    --backdrop: #d9d9d6;
    --card-light: #ffffff;
    --card-shade: #e4e4e4;
    --ink: #1c1c1c;
    --ink-soft: #3a3a3a;
    --teal: #1c8b98;
    --teal-deep: #14707b;
    --edge: #0d0d0d;
    --slogan: #e6f6f8;
  }
  * { margin: 0; padding: 0; box-sizing: border-box; }
  html, body {
    width: 1200px; height: 871px; overflow: hidden;
    background: var(--backdrop);
    font-family: "Questrial", "Century Gothic", sans-serif;
    color: var(--ink);
  }
  .sheet {
    position: relative; width: 1200px; height: 871px;
    display: flex; flex-direction: column; align-items: center; justify-content: center; gap: 60px;
  }
  .card {
    position: relative; width: 525px; height: 300px; overflow: hidden;
    background: linear-gradient(160deg, var(--card-light) 0%, var(--card-light) 45%, var(--card-shade) 100%);
    box-shadow: 0 10px 24px rgba(0,0,0,0.22);
  }
  .card-band { position: absolute; inset: 0; width: 100%; height: 100%; }
  .brand {
    position: absolute; display: flex; align-items: center; gap: 12px;
  }
  .brand-dot {
    width: 30px; height: 30px; border-radius: 50%; background: var(--ink);
  }
  .brand-name {
    font-size: 21px; letter-spacing: 2px; text-transform: uppercase; color: var(--ink); line-height: 1;
  }
  .card--front .brand { left: 50%; top: 108px; transform: translateX(-50%); }
  .slogan {
    position: absolute; left: 0; right: 0; bottom: 14px; text-align: center;
    font-size: 12px; letter-spacing: 3px; color: var(--slogan);
  }
  .card--back .brand { right: 34px; top: 44px; }
  .card--back .brand-name { font-size: 18px; }
  .card--back .brand-dot { width: 26px; height: 26px; }
  .holder {
    position: absolute; left: 36px; top: 118px;
    font-size: 14px; font-weight: 400; letter-spacing: 2px; color: var(--ink);
  }
  .address {
    position: absolute; left: 36px; top: 150px;
    font-size: 10.5px; line-height: 1.5; letter-spacing: 1.2px; color: var(--ink-soft);
    font-style: normal;
  }
  .contact {
    position: absolute; left: 270px; top: 190px; list-style: none;
    font-size: 11px; letter-spacing: 1.4px; color: var(--ink-soft);
  }
  .contact li { display: flex; align-items: center; gap: 10px; margin-bottom: 6px; }
  .contact svg { width: 12px; height: 12px; flex: none; }
</style>
</head>
<body>
<main class="sheet">

  <section class="card card--front" aria-label="Card front">
    <svg class="card-band" viewBox="0 0 525 300" preserveAspectRatio="none" aria-hidden="true">
      <path d="M0 236 Q250 300 525 246 L525 300 L0 300 Z" fill="var(--edge)"/>
      <path d="M0 242 Q250 306 525 252 L525 300 L0 300 Z" fill="var(--teal)"/>
    </svg>
    <div class="brand">
      <span class="brand-dot"></span>
      <span class="brand-name">Kestrel Bay Framing</span>
    </div>
    <p class="slogan">Building Dreams</p>
  </section>

  <section class="card card--back" aria-label="Card back">
    <svg class="card-band" viewBox="0 0 525 300" preserveAspectRatio="none" aria-hidden="true">
      <path d="M0 228 Q250 302 525 262 L525 300 L0 300 Z" fill="var(--edge)"/>
      <path d="M0 234 Q250 308 525 268 L525 300 L0 300 Z" fill="var(--teal)"/>
    </svg>
    <div class="brand">
      <span class="brand-dot"></span>
      <span class="brand-name">Kestrel Bay Framing</span>
    </div>
    <h1 class="holder">Dennis Harcourt</h1>
    <address class="address">
      #5 - 1845 Larchmont Way<br>
      Surrey, B.C. V7T 3K2
    </address>
    <ul class="contact">
      <li>
        <svg viewBox="0 0 12 12" aria-hidden="true"><path d="M2 1.5 L4.5 1.5 L5.2 3.8 L3.8 4.8 Q5 7.2 7.2 8.2 L8.2 6.8 L10.5 7.5 L10.5 10 Q5 10.5 1.6 5 Z" fill="var(--teal-deep)"/></svg>
        604.555.0193
      </li>
      <li>
        <svg viewBox="0 0 12 12" aria-hidden="true"><rect x="1" y="2.5" width="10" height="7" fill="none" stroke="var(--teal-deep)" stroke-width="1.2"/><path d="M1 2.5 L6 6.5 L11 2.5" fill="none" stroke="var(--teal-deep)" stroke-width="1.2"/></svg>
        dennisharcourt@telvane.ca
      </li>
    </ul>
  </section>

</main>
</body>
</html>
```